Home page for local retail aggregator

About us: We are a new company that showcases beautiful products available at nearby retail stores. This homepage is meant to display the latest products featured on our site and also allow the user to search, browse with filters, and access their account details.

Currently, our home page looks a little bland. We want the focus of the site to remain on the featured photos and products but the design should be more cohesive. The most successful designs will make more subtle use of our colors, provide intuitive menu controls, and look visually stunning.

This homepage has a few sections:

Header:
-Top Section: will always remain at the top of the page. There should be space for our company name ”zLantern”, a tagline, and a place for the menus.
-Menus: user must be able to find links for: “My profile” “My Products” “Add Product” “Preview store”
-Bottom section: this will scroll with the user and always remain at the top of the screen providing access to a search box, and filters for “location” “price” and retail categories.

Main Page:
-Each product featured is shown on a tile that includes a photo, title, price, name of store, has space to leave a comment, and include counters for "likes," comments, and "Pods"). “Pods” are bookmark folders. The user’s profile pic is also shown in miniature if they leave a comment.

The final version of the site must be delivered in a fully layered photoshop file and have versions demonstrating what the page will look like both when a user is logged-in and when logged-out.

Target Market(s)

Most of our users are female 18-45. Our customers are retail store owners who want their products to look attractive and professional.

Industry/Entity Type

Retail

Requirements
Must have
• Our logo must be present on the site (attached to project). You're welcome to change the colors in the header but it should look good with our logo.

For reference here are colors we're currently using:
Site text is in Dark Blue: RGB(10/23/47)
Logo color on business cards is light blue: (51/153/204)
Nice to have
• Would love to see new versions of the menus that are more modern and intuitive. Currently we just have links to each individual control. Putting these in a drop-down or re-arranging them would be nice.

```html
<!DOCTYPE html>
<html lang="en">
<head>
<meta charset="utf-8">
<title>zLantern – Local Product Search &amp; Discovery</title>
<link rel="stylesheet" href="https://fonts.googleapis.com/css2?family=Open+Sans:wght@400;600;700&family=Noto+Serif:ital,wght@1,400;1,700&display=swap">
<style>
:root{
  --purple-dark:#25123f;
  --purple:#3b2160;
  --purple-mid:#4a2b72;
  --sky:#3399cc;
  --sky-light:#5bb3e0;
  --ink:#0a172f;
  --muted:#8a8a8a;
  --price:#d9352a;
  --page:#eeeeec;
  --tile-line:#d9d9d9;
  --tile-foot:#ececec;
  --white:#ffffff;
}
*{box-sizing:border-box;margin:0;padding:0}
html,body{width:690px;height:1200px;overflow:hidden}
body{position:relative;background:var(--page);font-family:"Open Sans",Arial,sans-serif;color:var(--ink)}

/* Header */
.site-header{position:absolute;top:0;left:0;width:690px;height:70px;background:linear-gradient(180deg,var(--purple-mid),var(--purple-dark));}
.brand{position:absolute;left:22px;top:8px;display:flex;align-items:center;gap:14px}
.brand-mark{width:58px;height:58px;border-radius:50%;background:var(--sky-light)}
.brand-name{font-size:21px;font-weight:700;color:var(--white);line-height:1}
.brand-tagline{font-size:11px;font-weight:600;color:var(--sky-light);margin-top:6px}
.account{position:absolute;right:28px;top:16px;display:flex;gap:22px;font-size:7.5px;color:var(--sky-light)}
.account .welcome{display:flex;align-items:center;gap:4px}
.main-nav{position:absolute;right:25px;top:40px;display:flex;gap:12px;font-size:7.5px;font-weight:700;color:var(--white)}
.main-nav a{color:inherit;text-decoration:none}
.main-nav a::before{content:"• ";}

.search-band{position:absolute;top:70px;left:0;width:690px;height:25px;background:var(--sky-light);border-bottom:2px solid #c9d9e2}
.search-box{position:absolute;left:430px;top:3px;width:127px;height:18px;background:var(--white);border-radius:3px;display:flex;align-items:center;justify-content:space-between;padding:0 5px;font-family:"Noto Serif",Georgia,serif;font-style:italic;font-size:8px;color:var(--muted)}
.social{position:absolute;left:602px;top:3px;display:flex;gap:4px}
.social span{width:18px;height:18px;border-radius:3px;display:block}
.social .s1{background:#3b5998}.social .s2{background:#4fb6e8}.social .s3{background:#cb2027}

/* Product wall */
.wall{position:absolute;top:129px;left:28px;display:grid;grid-template-columns:repeat(5,120px);column-gap:8.5px;align-items:start}
.column{display:flex;flex-direction:column;gap:9px}
.tile{background:var(--white);border:1px solid var(--tile-line);box-shadow:0 1px 2px rgba(0,0,0,.12);padding-top:7px}
.tile-photo{margin:0 7px}
.tile-head{display:flex;justify-content:space-between;align-items:baseline;padding:7px 7px 0}
.tile-head h3{font-size:7px;font-weight:700;color:#222}
.price{font-family:"Noto Serif",Georgia,serif;font-style:italic;font-size:9px;color:var(--price)}
.store{font-family:"Noto Serif",Georgia,serif;font-style:italic;font-size:6px;color:var(--muted);padding:0 7px;line-height:9px}
.counts{list-style:none;display:flex;gap:7px;font-size:5px;color:#555;padding:7px 5px 4px}
.comment{background:var(--tile-foot);padding:4px 5px;display:flex;gap:5px;align-items:center;height:27px}
.avatar{width:15px;height:15px;flex:none}
.comment-field{flex:1;height:17px;background:var(--white);border:1px solid #d4d4d4;font-family:"Noto Serif",Georgia,serif;font-style:italic;font-size:5.5px;color:var(--muted);padding:4px 4px}

/* Filter panel */
.filter-label{position:absolute;left:27px;top:1113px;font-size:8.5px;font-weight:700;color:#333}
.filter-arrow{position:absolute;left:98px;top:1116px}
.scroll-top{position:absolute;left:603px;top:1100px;width:52px;height:30px;background:#f6f6f6;border:1px solid #cfcfcf;font-size:7px;font-weight:700;color:#333;padding:6px 5px;line-height:9px}
.scroll-top svg{position:absolute;right:5px;top:9px}
.filter-panel{position:absolute;left:25px;top:1133px;width:640px;height:90px;background:#f9f9f9;border:1px solid #d6d6d6;border-radius:6px}
.filter{position:absolute;top:22px;width:140px;height:25px;background:var(--purple);color:var(--white);font-size:8.5px;font-weight:700;display:flex;align-items:center;justify-content:space-between;padding:0 8px;border-radius:2px}
.filter::after{content:"";border:5px solid transparent;border-top:5px solid var(--white);margin-top:5px}
.f1{left:21px}.f2{left:187px}.f3{left:354px}
.search-now{position:absolute;left:516px;top:22px;width:101px;height:25px;background:linear-gradient(180deg,#6fc3ef,var(--sky));color:var(--white);font-size:8.5px;font-weight:700;display:flex;align-items:center;justify-content:center;gap:4px;border-radius:3px}
</style>
</head>
<body>

<header class="site-header">
  <div class="brand">
    <span class="brand-mark"></span>
    <div>
      <div class="brand-name">zLantern</div>
      <div class="brand-tagline">Local Product Search &amp; Discovery</div>
    </div>
  </div>
  <div class="account">
    <span class="welcome"><svg width="8" height="8" viewBox="0 0 8 8"><circle cx="4" cy="2.3" r="2" fill="#5bb3e0"/><path d="M0 8c0-2.5 2-3.5 4-3.5S8 5.5 8 8z" fill="#5bb3e0"/></svg>Welcome, Jamie Cole</span>
    <span>Logout</span>
  </div>
  <nav class="main-nav">
    <a href="#">My Profile</a><a href="#">My Product</a><a href="#">Add Product</a><a href="#">Preview Store</a>
  </nav>
</header>

<div class="search-band">
  <div class="search-box">Search here
    <svg width="10" height="10" viewBox="0 0 10 10"><circle cx="4" cy="4" r="3" fill="none" stroke="#111" stroke-width="1.6"/><path d="M6.3 6.3L9.3 9.3" stroke="#111" stroke-width="1.8"/></svg>
  </div>
  <div class="social"><span class="s1"></span><span class="s2"></span><span class="s3"></span></div>
</div>

<main class="wall">
  <div class="column">
    <article class="tile"><div class="tile-photo" role="img" aria-label="Painted wall crosses" style="height:122px;background:linear-gradient(135deg,#8ab6c8,#b0488a,#e0b040)"></div><div class="tile-head"><h3>Crosses - Rosa</h3><span class="price">$62</span></div><p class="store">Minimal</p><ul class="counts"><li>50 Likes</li><li>2 Comments</li><li>15 Pods</li></ul><div class="comment"><span class="avatar" role="img" aria-label="Commenter avatar" style="background:#e6c890"></span><span class="comment-field">What do you think?</span></div></article>
    <article class="tile"><div class="tile-photo" role="img" aria-label="Denim shirt on a model" style="height:123px;background:linear-gradient(180deg,#f2f2f2,#8fa8c0 50%,#2a2a2a)"></div><div class="tile-head"><h3>Shirt</h3><span class="price">$120</span></div><p class="store">Minimal</p><ul class="counts"><li>50 Likes</li><li>2 Comments</li><li>15 Pods</li></ul><div class="comment"><span class="avatar" role="img" aria-label="Commenter avatar" style="background:#c07840"></span><span class="comment-field">What do you think?</span></div></article>
    <article class="tile"><div class="tile-photo" role="img" aria-label="Painted wall crosses" style="height:124px;background:linear-gradient(135deg,#8ab6c8,#b0488a,#e0b040)"></div><div class="tile-head"><h3>Crosses - Rosa</h3><span class="price">$62</span></div><p class="store">Minimal</p><ul class="counts"><li>50 Likes</li><li>2 Comments</li><li>15 Pods</li></ul><div class="comment"><span class="avatar" role="img" aria-label="Commenter avatar" style="background:#e6c890"></span><span class="comment-field">What do you think?</span></div></article>
    <article class="tile"><div class="tile-photo" role="img" aria-label="Green bmx bicycle" style="height:68px;background:linear-gradient(180deg,#e8e4e0,#b8c0a8)"></div><div class="tile-head"><h3>mûûû mûûûû!!</h3><span class="price">$100</span></div><p class="store">Minimal</p><ul class="counts"><li>50 Likes</li><li>2 Comments</li><li>15 Pods</li></ul><div class="comment"><span class="avatar" role="img" aria-label="Commenter avatar" style="background:#c07840"></span><span class="comment-field">What do you think?</span></div></article>
  </div>

  <div class="column">
    <article class="tile"><div class="tile-photo" role="img" aria-label="Floral casual top on a model" style="height:126px;background:linear-gradient(180deg,#f4f4f4,#3a2e2e 40%,#5a4038)"></div><div class="tile-head"><h3>Casual Tops</h3><span class="price">$58</span></div><p class="store">Minimal</p><ul class="counts"><li>50 Likes</li><li>2 Comments</li><li>15 Pods</li></ul><div class="comment"><span class="avatar" role="img" aria-label="Commenter avatar" style="background:#b89070"></span><span class="comment-field">What do you think?</span></div></article>
    <article class="tile"><div class="tile-photo" role="img" aria-label="Old metal lantern outdoors" style="height:103px;background:linear-gradient(135deg,#3a6a30,#8aa060,#5a5040)"></div><div class="tile-head"><h3>Old Lantern</h3><span class="price">$450</span></div><p class="store">Minimal</p><ul class="counts"><li>50 Likes</li><li>2 Comments</li><li>15 Pods</li></ul><div class="comment"><span class="avatar" role="img" aria-label="Commenter avatar" style="background:#c07840"></span><span class="comment-field">What do you think?</span></div></article>
    <article class="tile"><div class="tile-photo" role="img" aria-label="Swirling colourful paper art" style="height:80px;background:linear-gradient(135deg,#c04040,#4aa0b0,#e0b060)"></div><div class="tile-head"><h3>Lorem Lipsum</h3><span class="price">$249</span></div><p class="store">Minimal</p><ul class="counts"><li>50 Likes</li><li>2 Comments</li><li>15 Pods</li></ul><div class="comment"><span class="avatar" role="img" aria-label="Commenter avatar" style="background:#c07840"></span><span class="comment-field">What do you think?</span></div></article>
    <article class="tile"><div class="tile-photo" role="img" aria-label="Duct tape flowers" style="height:67px;background:linear-gradient(90deg,#e04040,#f0a020,#30a0d0)"></div><div class="tile-head"><h3>Duct Tape Flowers</h3><span class="price">$55</span></div><p class="store">Minimal</p><ul class="counts"><li>50 Likes</li><li>2 Comments</li><li>15 Pods</li></ul><div class="comment"><span class="avatar" role="img" aria-label="Commenter avatar" style="background:#c07840"></span><span class="comment-field">What do you think?</span></div></article>
    <article class="tile"><div class="tile-photo" role="img" aria-label="Stained glass candle ornament" style="height:100px;background:linear-gradient(180deg,#f2f2f0,#d8e0c8,#4a8a40)"></div><div class="tile-head"><h3>Bling Eye Mackup</h3><span class="price">$19</span></div><p class="store">Minimal</p><ul class="counts"><li>50 Likes</li><li>2 Comments</li><li>15 Pods</li></ul><div class="comment"><span class="avatar" role="img" aria-label="Commenter avatar" style="background:#404a70"></span><span class="comment-field">What do you think?</span></div></article>
  </div>

  <div class="column">
    <article class="tile"><div class="tile-photo" role="img" aria-label="Glitter eye makeup" style="height:67px;background:linear-gradient(180deg,#e8c8c8,#3a3848 50%,#d8b8b8)"></div><div class="tile-head"><h3>Bling Eye Mackup</h3><span class="price">$12</span></div><p class="store">Minimal</p><ul class="counts"><li>50 Likes</li><li>2 Comments</li><li>15 Pods</li></ul><div class="comment"><span class="avatar" role="img" aria-label="Commenter avatar" style="background:#c07840"></span><span class="comment-field">What do you think?</span></div></article>
    <article class="tile"><div class="tile-photo" role="img" aria-label="Green bmx bicycle" style="height:63px;background:linear-gradient(180deg,#e8e4e0,#b8c0a8)"></div><div class="tile-head"><h3>mûûû mûûûû!!</h3><span class="price">$100</span></div><p class="store">Minimal</p><ul class="counts"><li>50 Likes</li><li>2 Comments</li><li>15 Pods</li></ul><div class="comment"><span class="avatar" role="img" aria-label="Commenter avatar" style="background:#c07840"></span><span class="comment-field">What do you think?</span></div></article>
    <article class="tile"><div class="tile-photo" role="img" aria-label="Bikini by a pool" style="height:133px;background:linear-gradient(180deg,#5ac0e0,#c8a088 50%,#40b0d8)"></div><div class="tile-head"><h3>Bikini</h3><span class="price">$499</span></div><p class="store">Minimal</p><ul class="counts"><li>50 Likes</li><li>2 Comments</li><li>15 Pods</li></ul><div class="comment"><span class="avatar" role="img" aria-label="Commenter avatar" style="background:#c07840"></span><span class="comment-field">What do you think?</span></div></article>
    <article class="tile"><div class="tile-photo" role="img" aria-label="Glitter eye makeup" style="height:69px;background:linear-gradient(180deg,#e8c8c8,#3a3848 50%,#d8b8b8)"></div><div class="tile-head"><h3>Bling Eye Mackup</h3><span class="price">$12</span></div><p class="store">Minimal</p><ul class="counts"><li>50 Likes</li><li>2 Comments</li><li>15 Pods</li></ul><div class="comment"><span class="avatar" role="img" aria-label="Commenter avatar" style="background:#c07840"></span><span class="comment-field">What do you think?</span></div></article>
    <article class="tile"><div class="tile-photo" role="img" aria-label="Denim shirt on a model" style="height:129px;background:linear-gradient(180deg,#f2f2f2,#8fa8c0 50%,#2a2a2a)"></div><div class="tile-head"><h3>Shirt</h3><span class="price">$120</span></div><p class="store">Minimal</p><ul class="counts"><li>50 Likes</li><li>2 Comments</li><li>15 Pods</li></ul><div class="comment"><span class="avatar" role="img" aria-label="Commenter avatar" style="background:#c07840"></span><span class="comment-field">What do you think?</span></div></article>
  </div>

  <div class="column">
    <article class="tile"><div class="tile-photo" role="img" aria-label="Stained glass candle ornament" style="height:97px;background:linear-gradient(180deg,#f2f2f0,#e8d070 40%,#4a8a40)"></div><div class="tile-head"><h3>Bling Eye Mackup</h3><span class="price">$19</span></div><p class="store">Minimal</p><ul class="counts"><li>50 Likes</li><li>2 Comments</li><li>15 Pods</li></ul><div class="comment"><span class="avatar" role="img" aria-label="Commenter avatar" style="background:#404a70"></span><span class="comment-field">What do you think?</span></div></article>
    <article class="tile"><div class="tile-photo" role="img" aria-label="Duct tape flowers" style="height:70px;background:linear-gradient(90deg,#e04040,#f0a020,#30a0d0)"></div><div class="tile-head"><h3>Duct Tape Flowers</h3><span class="price">$55</span></div><p class="store">Minimal</p><ul class="counts"><li>50 Likes</li><li>2 Comments</li><li>15 Pods</li></ul><div class="comment"><span class="avatar" role="img" aria-label="Commenter avatar" style="background:#c07840"></span><span class="comment-field">What do you think?</span></div></article>
    <article class="tile"><div class="tile-photo" role="img" aria-label="Yellow and grey fleece scarf" style="height:129px;background:linear-gradient(180deg,#f6f6f6,#9aa0b8 45%,#e8c040)"></div><div class="tile-head"><h3>Fleece Scarf</h3><span class="price">$60</span></div><p class="store">Minimal</p><ul class="counts"><li>50 Likes</li><li>2 Comments</li><li>15 Pods</li></ul><div class="comment"><span class="avatar" role="img" aria-label="Commenter avatar" style="background:#c07840"></span><span class="comment-field">What do you think?</span></div></article>
    <article class="tile"><div class="tile-photo" role="img" aria-label="Floral casual top on a model" style="height:129px;background:linear-gradient(180deg,#f4f4f4,#3a2e2e 40%,#5a4038)"></div><div class="tile-head"><h3>Casual Tops</h3><span class="price">$58</span></div><p class="store">Minimal</p><ul class="counts"><li>50 Likes</li><li>2 Comments</li><li>15 Pods</li></ul><div class="comment"><span class="avatar" role="img" aria-label="Commenter avatar" style="background:#b89070"></span><span class="comment-field">What do you think?</span></div></article>
    <article class="tile"><div class="tile-photo" role="img" aria-label="Purple bmx bicycle" style="height:70px;background:linear-gradient(180deg,#e8e4e0,#a8a0c0)"></div><div class="tile-head"><h3>mûûû mûûûû!!</h3><span class="price">$100</span></div><p class="store">Minimal</p><ul class="counts"><li>50 Likes</li><li>2 Comments</li><li>15 Pods</li></ul><div class="comment"><span class="avatar" role="img" aria-label="Commenter avatar" style="background:#c07840"></span><span class="comment-field">What do you think?</span></div></article>
  </div>

  <div class="column">
    <article class="tile"><div class="tile-photo" role="img" aria-label="Dark blue jeans on a model" style="height:204px;background:linear-gradient(180deg,#f0f0f0,#1e2c50 20%,#2a3a60 85%,#e8e8e8)"></div><div class="tile-head"><h3>Jeans</h3><span class="price">$250</span></div><p class="store">Minimal</p><ul class="counts"><li>50 Likes</li><li>2 Comments</li><li>15 Pods</li></ul><div class="comment"><span class="avatar" role="img" aria-label="Commenter avatar" style="background:#c07840"></span><span class="comment-field">What do you think?</span></div></article>
    <article class="tile"><div class="tile-photo" role="img" aria-label="Tufted coffee table in a living room" style="height:138px;background:linear-gradient(180deg,#c8c0b0,#f0ece4 55%,#4a4038)"></div><div class="tile-head"><h3>Coffee Table</h3><span class="price">$259</span></div><p class="store">Minimal</p><ul class="counts"><li>50 Likes</li><li>2 Comments</li><li>15 Pods</li></ul><div class="comment"><span class="avatar" role="img" aria-label="Commenter avatar" style="background:#c07840"></span><span class="comment-field">What do you think?</span></div></article>
    <article class="tile"><div class="tile-photo" role="img" aria-label="Painted wall crosses" style="height:125px;background:linear-gradient(135deg,#8ab6c8,#b0488a,#e0b040)"></div><div class="tile-head"><h3>Crosses - Rosa</h3><span class="price">$62</span></div><p class="store">Minimal</p><ul class="counts"><li>50 Likes</li><li>2 Comments</li><li>15 Pods</li></ul><div class="comment"><span class="avatar" role="img" aria-label="Commenter avatar" style="background:#e6c890"></span><span class="comment-field">What do you think?</span></div></article>
    <article class="tile"><div class="tile-photo" role="img" aria-label="Old metal lantern outdoors" style="height:104px;background:linear-gradient(135deg,#7a3a30,#b87860,#5a4a40)"></div><div class="tile-head"><h3>Old Lantern</h3><span class="price">$450</span></div><p class="store">Minimal</p><ul class="counts"><li>50 Likes</li><li>2 Comments</li><li>15 Pods</li></ul><div class="comment"><span class="avatar" role="img" aria-label="Commenter avatar" style="background:#c07840"></span><span class="comment-field">What do you think?</span></div></article>
  </div>
</main>

<div class="filter-label">Search by Filter</div>
<svg class="filter-arrow" width="40" height="16" viewBox="0 0 40 16"><path d="M1 2 Q 25 0 33 12" fill="none" stroke="#666" stroke-width="1"/><path d="M30 10 L34 14 L35 8" fill="none" stroke="#666" stroke-width="1"/></svg>

<div class="scroll-top">Scroll<br>To Top
  <svg width="10" height="12" viewBox="0 0 10 12"><path d="M5 0 L9 6 H6.5 V12 H3.5 V6 H1 Z" fill="#3b2160"/></svg>
</div>

<section class="filter-panel">
  <div class="filter f1">By Location</div>
  <div class="filter f2">By Price</div>
  <div class="filter f3">By Retail Categories</div>
  <div class="search-now">SEARCH NOW!
    <svg width="10" height="10" viewBox="0 0 10 10"><circle cx="4" cy="4" r="3" fill="none" stroke="#fff" stroke-width="1.6"/><path d="M6.3 6.3L9.3 9.3" stroke="#fff" stroke-width="1.8"/></svg>
  </div>
</section>

</body>
</html>
```